Business Card Needed for Crafter of Pottery, Jewelry and Artwork

Calling all designers in search of an artistic challenge.

I need a new business card design for my pottery, jewelry and artwork business, Woven Glass and Tide, based in Vancouver BC.

I would like a card that is bright and inviting and preferably incorporates my logo and a sample of photos of my work while having a clean fresh look. The following contact details would preferably be included on the card as well:
• Helena Pikeworth
• Designer
• Phone: 604.555.0172
• Email: Designer@WovenGlassandTide.example
• Website: www.WovenGlassandTide.example
• Blog: www.ShapingHillside.example

The logo is attached in two color schemes in both Vector and Source formats. On past cards I’ve also included photos of my work. By including photos of the work the pieces are showcased and it catches people’s eye and prompts them to pick up the card and look at it more closely. For example, if I leave a stack in a coffee shop I want people to be drawn to the card, to pick it up and get a sense of the my product lines. Please feel free to pull photos of my work directly off of my website. If you need photos with higher pixels please let me know and I’ll email them directly to you. The website background is bffbda (191, 251, 218). I would like the business cards to match the feel of the website for consistency but the cards do not need to use the exact same colors. My website and current business card are predominantly turquoise shades. The background uses stripes provided by the website template. I don’t know the exact colors of the stripes.

My current business card is attached to show the use of photos in a design. Please note that I am not thrilled with my own design and am looking for variations and completely new designs. This example is not meant to be used as a template or starting point.

Here is some background surrounding my company:
WGT offers one of a kind jewelry, pottery, artwork and leather bags each designed with a twist. The pottery varies from rustic every day functional ware to raku artwork. The jewelry ranges from simple sterling every day pieces to multimedia pieces incorporating stone, metal, ceramics and fabric. The artwork is multimedia, typically acrylic paired with a natural element such as bark. All the bags are leather with reworked kimono fabric or patterned silk lining.

Feel free to check out my website to get a flavour for my work and the color scheme I've used on marketing materials so far. www.wovenglassandtide.example
Updates

Thank you to everyone who has submitted a design so far. I hope everyone has received some helpful feedback.

I'm going to post a survey to customers and friends asking for their votes. If you have new designs to submit please try to get them in by Saturday March 30 at noon so that I can include it in the survey launch.

Thank you

Target Market(s)

Females aged 25-65 interested in one of a kind functional pottery and jewelry.

Industry/Entity Type

Coffee Shop

Requirements
Must have
• Contact information, website, blog
Nice to have
• Logo, photos

```html
<!DOCTYPE html>
<html lang="en">
<head>
<meta charset="utf-8">
<title>Woven Glass and Tide — Business Card</title>
<link rel="stylesheet" href="https://fonts.googleapis.com/css2?family=Source+Sans+3:wght@400;600&display=swap">
<style>
  :root {
    --canvas: #ffffff;
    --card-white: #ffffff;
    --navy: #22215a;
    --teal: #3fbfb3;
    --teal-deep: #16b1a6;
    --teal-back: #52c7be;
    --aqua-light: #e6ffff;
    --aqua-bright: #4ff6f6;
    --ink: #3c3c46;
    --muted: #5a5a66;
  }
  * { box-sizing: border-box; margin: 0; padding: 0; }
  html, body {
    width: 1200px; height: 1000px; overflow: hidden;
    background: var(--canvas);
    font-family: "Source Sans 3", "Myriad Pro", Arial, sans-serif;
  }
  .card {
    position: absolute;
    left: 282px;
    width: 636px; height: 364px;
    border-radius: 22px;
    overflow: hidden;
    box-shadow: 0 4px 10px rgba(0,0,0,0.25);
  }
  .card--front { top: 108px; background: var(--card-white); }
  .card--back  { top: 528px; background: var(--teal-back); }
  .card__waves { position: absolute; inset: 0; width: 100%; height: 100%; }
  .card__footer-url {
    position: absolute; left: 0; right: 0;
    text-align: center; color: #fff;
    font-size: 15px; letter-spacing: 0.2px;
  }
  .card--front .card__footer-url { top: 326px; }
  .card--back .card__footer-url { top: 326px; }

  .brand-mark {
    position: absolute;
    border-radius: 50%;
    background: var(--teal-deep);
    display: flex; align-items: center; justify-content: center;
    text-align: center; color: #fff; font-weight: 600;
    line-height: 1.15;
  }
  .card--front .brand-mark {
    left: 58px; top: 98px; width: 140px; height: 140px;
    box-shadow: 0 0 0 5px #fff, 0 0 0 8px var(--teal-deep);
    font-size: 17px; padding: 0 18px;
  }
  .card--back .brand-mark {
    left: 192px; top: 42px; width: 252px; height: 252px;
    box-shadow: 0 0 0 8px #fff, 0 0 0 12px #3fb9b0;
    font-size: 28px; padding: 0 34px;
  }

  .contact { position: absolute; left: 307px; top: 78px; }
  .contact__name { color: var(--teal); font-size: 24px; font-weight: 600; line-height: 1.1; }
  .contact__role { color: var(--muted); font-size: 15px; margin-top: 3px; }
  .contact__list { list-style: none; margin-top: 20px; }
  .contact__item {
    display: flex; align-items: center; gap: 5px;
    color: var(--ink); font-size: 15px; line-height: 21.5px;
  }
  .contact__icon { width: 14px; height: 14px; flex: none; }
</style>
</head>
<body>

<section class="card card--front" aria-label="Business card front">
  <svg class="card__waves" viewBox="0 0 636 364" preserveAspectRatio="none" aria-hidden="true">
    <defs>
      <linearGradient id="aquaFront" x1="0" x2="1" y1="0" y2="0">
        <stop offset="0" stop-color="#ffffff"/>
        <stop offset="0.45" stop-color="#c8fbfb"/>
        <stop offset="1" stop-color="#4ff6f6"/>
      </linearGradient>
    </defs>
    <path d="M0 246 C 160 262, 360 300, 636 238 L636 364 L0 364 Z" fill="url(#aquaFront)"/>
    <path d="M0 252 C 150 300, 380 312, 636 294 L636 364 L0 364 Z" fill="#22215a"/>
  </svg>

  <div class="brand-mark">Woven Glass and Tide</div>

  <div class="contact">
    <h1 class="contact__name">Helena Pikeworth</h1>
    <p class="contact__role">Designer</p>
    <ul class="contact__list">
      <li class="contact__item">
        <svg class="contact__icon" viewBox="0 0 14 14" aria-hidden="true"><path d="M1 5 Q7 0 13 5 L11 7 L9 5.5 L5 5.5 L3 7 Z M3 8 H11 L12 12 H2 Z" fill="#3fbfb3"/></svg>
        604.555.0172
      </li>
      <li class="contact__item">
        <svg class="contact__icon" viewBox="0 0 14 14" aria-hidden="true"><rect x="1" y="3" width="12" height="8.5" fill="#3fbfb3"/><path d="M1 3 L7 8 L13 3" stroke="#fff" stroke-width="1.2" fill="none"/></svg>
        Designer@WovenGlassandTide.example
      </li>
      <li class="contact__item">
        <svg class="contact__icon" viewBox="0 0 14 14" aria-hidden="true"><circle cx="7" cy="7" r="5.8" fill="none" stroke="#3fbfb3" stroke-width="1.4"/><ellipse cx="7" cy="7" rx="2.4" ry="5.8" fill="none" stroke="#3fbfb3" stroke-width="1.1"/><path d="M1.2 7 H12.8" stroke="#3fbfb3" stroke-width="1.1"/></svg>
        www.WovenGlassandTide.example
      </li>
      <li class="contact__item">
        <svg class="contact__icon" viewBox="0 0 14 14" aria-hidden="true"><rect x="1.5" y="1.5" width="11" height="11" rx="2.5" fill="#3fbfb3"/></svg>
        www.ShapingHillside.example
      </li>
    </ul>
  </div>

  <p class="card__footer-url">www.ShapingHillside.example</p>
</section>

<section class="card card--back" aria-label="Business card back">
  <svg class="card__waves" viewBox="0 0 636 364" preserveAspectRatio="none" aria-hidden="true">
    <defs>
      <linearGradient id="aquaBack" x1="0" x2="1" y1="0" y2="0">
        <stop offset="0" stop-color="#ffffff"/>
        <stop offset="0.45" stop-color="#c8fbfb"/>
        <stop offset="1" stop-color="#4ff6f6"/>
      </linearGradient>
    </defs>
    <path d="M0 238 C 160 256, 360 296, 636 230 L636 364 L0 364 Z" fill="url(#aquaBack)"/>
    <path d="M0 244 C 150 292, 380 306, 636 288 L636 364 L0 364 Z" fill="#22215a"/>
  </svg>

  <div class="brand-mark">Woven Glass and Tide</div>

  <p class="card__footer-url">www.ShapingHillside.example</p>
</section>

</body>
</html>
```